Simple Website Design for Law Office

I need a website design for our law office (Law Offices of Marcus Pellow) that is extremely simple, only including a landing page and perhaps a contact page (parallax scrolling).

Website should look similar to this one (template): https://www.brightfenwaystudio.com/

Design should be modern, simple, and inviting. There are a few assets like logo, stock photos/icons we would like added as well, and some language and contact info, but very basic stuff.

The name of the company is: Law Offices of Marcus Pellow

Target Market(s)

B2B corporate clients, users from Canada, UK, East Asia, and all potential users with immigration needs

Coding

Coded - Design and coding required

Number of Pages Required

2 page

Colors

Designer to choose colors to be used in the design.

Requirements
Must have
• Landing page, Contact Page
• Simple, elegant design with minimalist font
Nice to have
• Parallax scrolling, so one page and can scroll to contact us segment

```html
<!DOCTYPE html>
<html lang="en">
<head>
<meta charset="utf-8">
<title>Law Offices of Marcus Pellow — Immigration Law Firm</title>
<link href="https://fonts.googleapis.com/css2?family=Montserrat:wght@300;400;500;600;700&display=swap" rel="stylesheet">
<style>
:root{
  --navy:#0b3272;
  --link:#1d4f9e;
  --ink:#111;
  --muted:#6a6a6a;
  --line:#dcdcdc;
  --soft:#f6f6f6;
  --footer:#1f1f1f;
  --footer-bottom:#171717;
  --white:#fff;
}
*{margin:0;padding:0;box-sizing:border-box}
html,body{width:1200px;height:3909px;overflow:hidden}
body{font-family:'Montserrat',sans-serif;color:var(--ink);background:var(--white);position:relative}
.abs{position:absolute}
a{color:inherit;text-decoration:none}

/* hero */
.hero{left:0;top:0;width:1200px;height:716px;background:linear-gradient(180deg,#27527a 0%,#5b7d98 30%,#6b7880 55%,#3e4650 100%)}
.hero-shade{left:0;top:0;width:1200px;height:716px;background:linear-gradient(180deg,rgba(10,30,60,.25),rgba(0,0,0,.15))}
.nav a{position:absolute;top:62px;font-size:12px;font-weight:500;color:var(--white);letter-spacing:.3px}
.nav .active{border-bottom:2px solid var(--white);padding-bottom:8px}
.brand{left:450px;top:30px;width:300px;text-align:center;color:var(--white);font-weight:600;font-size:29px;line-height:37px;letter-spacing:.3px}
.hero-title{left:0;top:296px;width:1200px;text-align:center;color:var(--white);font-size:44px;font-weight:700;letter-spacing:.5px}
.hero-sub{left:0;top:355px;width:1200px;text-align:center;color:var(--white);font-size:22px;font-weight:300}
.hero-text{left:290px;top:404px;width:620px;text-align:center;color:var(--white);font-size:13px;line-height:22px}
.btn-outline{left:520px;top:472px;width:160px;height:46px;border:1px solid rgba(255,255,255,.8);color:var(--white);font-size:12px;display:flex;align-items:center;justify-content:center}

/* about */
.about{left:0;top:716px;width:1200px;height:326px;background:var(--soft)}
.about-img{left:640px;top:716px;width:560px;height:326px;background:linear-gradient(160deg,#f4f4f4 0%,#e8e6e4 40%,#b23a3a 70%,#2b3c6e 100%)}
.h-section{font-size:44px;font-weight:700;letter-spacing:.3px}
.about-title{left:115px;top:778px}
.about-sub{left:115px;top:848px;color:var(--link);font-size:20px;font-weight:400}
.about-text{left:115px;top:898px;width:470px;font-size:12px;line-height:21px;color:var(--muted)}

/* practice */
.practice-title{left:0;top:1110px;width:1200px;text-align:center}
.grid{left:188px;top:1227px;width:830px;height:363px;border:1px solid var(--line)}
.cell{position:absolute;text-align:center;padding-top:26px}
.cell svg{display:block;margin:0 auto 10px}
.cell h3{font-size:16px;font-weight:600;margin-bottom:8px}
.cell p{font-size:11.5px;line-height:21px;color:var(--muted);width:230px;margin:0 auto}
.vline{background:var(--line);width:1px}
.hline{background:var(--line);height:1px}
.featured{left:452px;top:1215px;width:302px;height:203px;background:var(--navy);box-shadow:0 10px 24px rgba(0,0,0,.3);color:var(--white);padding-top:40px}
.featured p{color:var(--white)}

/* attorneys */
.attorneys{left:0;top:1688px;width:1200px;height:531px;background:linear-gradient(135deg,#1f4b86 0%,#2c5a95 45%,#4f79ad 100%)}
.statue{left:850px;top:1630px;width:190px;height:589px;background:linear-gradient(180deg,#8fa79c 0%,#5f8f86 50%,#4e7a74 100%);border-radius:60px 60px 0 0}
.att-title{left:182px;top:1750px;color:var(--white)}
.profile{position:absolute;top:1852px;width:150px;color:var(--white)}
.photo{width:148px;height:213px;background:var(--white);padding:12px}
.photo div{width:100%;height:100%;background:linear-gradient(180deg,#b7b7b7,#555)}
.profile h4{margin-top:22px;font-size:16px;font-weight:600;white-space:nowrap}
.profile span{display:block;font-size:12px;margin-top:4px}
.profile i{display:block;width:148px;height:4px;background:var(--white);margin-top:12px}

/* resources */
.res-title{left:0;top:2283px;width:1200px;text-align:center}
.card{position:absolute;background:var(--white);box-shadow:0 4px 18px rgba(0,0,0,.08);padding:24px 12px 24px 22px}
.card h4{font-size:15px;font-weight:600;line-height:21px;margin-bottom:20px;white-space:nowrap}
.card dt{font-size:11px;color:var(--muted);margin-top:22px;white-space:nowrap}
.card dt:first-of-type{margin-top:0}
.card dd{font-size:11px;color:var(--link);margin-top:6px;white-space:nowrap}
.card .arrow{position:absolute;right:22px;bottom:14px}
.dot{position:absolute;top:2979px;width:8px;height:8px;border-radius:50%;background:#b7c4da}
.dot.on{background:var(--navy)}

/* contact */
.contact-bg{left:0;top:3045px;width:1200px;height:470px;background:linear-gradient(135deg,#a9c3e0 0%,#e3e5e6 45%,#c9c1b2 100%)}
.contact-panel{left:180px;top:3125px;width:418px;height:313px;background:var(--navy)}
.contact-title{left:219px;top:3162px;color:var(--white)}
.field{position:absolute;border:1px solid rgba(255,255,255,.8);color:var(--white);font-size:12px;padding:14px 12px}
.submit{left:219px;top:3367px;width:159px;height:45px;background:var(--white);color:var(--navy);font-size:12px;display:flex;align-items:center;justify-content:center}
.map{left:598px;top:3125px;width:420px;height:313px;background:linear-gradient(135deg,#e9ece4 0%,#dfe6dc 50%,#cfe0ea 100%)}

/* footer */
.footer{position:absolute;left:0;top:3515px;width:1200px;height:320px;background:var(--footer);color:#d0d0d0}
.footer h5{position:absolute;font-size:15px;font-weight:600;color:var(--white);line-height:19px}
.footer p{position:absolute;font-size:12px;line-height:21px}
.footer .icon{position:absolute}
.seal{left:505px;top:105px;width:135px;height:135px;border-radius:50%;background:var(--white)}
.social{position:absolute;top:240px;width:12px;height:12px;border-radius:50%;background:#bbb}
.bottom{left:0;top:3835px;width:1200px;height:74px;background:var(--footer-bottom);color:#cfcfcf;font-size:11px}
.bottom span{position:absolute;top:30px}
</style>
</head>
<body>

<header>
  <div class="abs hero" role="img" aria-label="Aerial photograph of a downtown city skyline with mountains behind"></div>
  <div class="abs hero-shade"></div>
  <nav class="nav">
    <a class="active" style="left:205px">HOME</a>
    <a style="left:275px">ATTORNEY PROFILES</a>
    <a style="left:795px">PRACTICE AREAS</a>
    <a style="left:943px">RESOURCES</a>
  </nav>
  <div class="abs brand">MARCUS PELLOW<br>LAW OFFICES</div>
  <h1 class="abs hero-title">IMMIGRATION LAW FIRM</h1>
  <p class="abs hero-sub">Law Offices of Marcus Pellow</p>
  <p class="abs hero-text">Established in 1978, the Law Offices of Marcus Pellow is a full service immigration law firm offering legal advice on a wide range of immigration related issues including family</p>
  <a class="abs btn-outline">CONTACT US</a>
</header>

<section>
  <div class="abs about"></div>
  <div class="abs about-img" role="img" aria-label="Citizenship and immigration document with a flag and pen"></div>
  <h2 class="abs h-section about-title">ABOUT US</h2>
  <p class="abs about-sub">U.S. IMMIGRATION LAW FIRM</p>
  <p class="abs about-text">Established in 1978, the Law Offices of Marcus Pellow is a full service immigration law firm offering legal advice on a wide range of immigration related issues including family and business based immigration, EB-5 investment, federal court litigation, appeals, consular processing and naturalization/citizenship.</p>
</section>

<section>
  <h2 class="abs h-section practice-title">PRACTICE AREAS</h2>
  <div class="abs grid">
    <div class="abs vline" style="left:276px;top:0;height:363px"></div>
    <div class="abs vline" style="left:552px;top:0;height:363px"></div>
    <div class="abs hline" style="left:0;top:181px;width:830px"></div>

    <div class="cell" style="left:0;top:0;width:276px">
      <svg width="36" height="42" viewBox="0 0 36 42" fill="none" stroke="#0b3272" stroke-width="2"><circle cx="12" cy="5" r="3"/><circle cx="24" cy="5" r="3"/><rect x="7" y="11" width="22" height="7"/><rect x="3" y="18" width="30" height="8"/><rect x="7" y="26" width="22" height="14"/></svg>
      <h3>Family</h3><p>The Law Offices of Marcus Pellow assists families to reunite and stay</p>
    </div>
    <div class="cell" style="left:552px;top:0;width:276px">
      <svg width="40" height="42" viewBox="0 0 40 42" fill="none" stroke="#0b3272" stroke-width="2"><path d="M20 3l14 6v12c0 10-7 16-14 19C13 37 6 31 6 21V9z"/><circle cx="20" cy="20" r="8"/><path d="M20 15l2 4h4l-3 3 1 4-4-2-4 2 1-4-3-3h4z"/></svg>
      <h3>Citizenship &amp; Naturalization</h3><p>The Law Offices of Marcus Pellow helps clients realize the dream</p>
    </div>
    <div class="cell" style="left:0;top:182px;width:276px">
      <svg width="40" height="42" viewBox="0 0 40 42" fill="none" stroke="#0b3272" stroke-width="2"><path d="M10 4h24v30a5 5 0 0 1-5 5H6a5 5 0 0 0 4-5z"/><path d="M15 12h14M15 18h14M15 24h10"/></svg>
      <h3>Litigation &amp; Appeals</h3><p>The Law Offices of Marcus Pellow litigates immigration-related</p>
    </div>
    <div class="cell" style="left:276px;top:182px;width:276px">
      <svg width="40" height="42" viewBox="0 0 40 42" fill="none" stroke="#0b3272" stroke-width="2"><path d="M3 14L20 4l17 10z"/><path d="M5 14h30M9 18v16M16 18v16M24 18v16M31 18v16M3 38h34M5 34h30"/></svg>
      <h3>Deportation &amp; Renewal</h3><p>The Law Offices of Marcus Pellow has significant experience</p>
    </div>
    <div class="cell" style="left:552px;top:182px;width:276px">
      <svg width="36" height="42" viewBox="0 0 36 42" fill="none" stroke="#0b3272" stroke-width="2"><circle cx="12" cy="5" r="3"/><circle cx="24" cy="5" r="3"/><rect x="7" y="11" width="22" height="7"/><rect x="3" y="18" width="30" height="8"/><rect x="7" y="26" width="22" height="14"/></svg>
      <h3>Family</h3><p>The Law Offices of Marcus Pellow assists families to reunite and stay</p>
    </div>
  </div>
  <div class="abs cell featured">
    <svg width="44" height="38" viewBox="0 0 44 38" fill="none" stroke="#fff" stroke-width="2"><rect x="3" y="9" width="38" height="26"/><path d="M15 9V3h14v6M3 17l19 9 19-9"/></svg>
    <h3>Investor and Entrepreneurs</h3><p>Law Offices of Marcus Pellow is highly regarded for extraordinary</p>
  </div>
</section>

<section>
  <div class="abs attorneys" role="img" aria-label="Blue-toned photograph of a classical government building"></div>
  <div class="abs statue" role="img" aria-label="Photograph of a torch-bearing statue"></div>
  <h2 class="abs h-section att-title">ATTORNEY PROFILES</h2>
  <div class="profile" style="left:182px"><div class="photo" role="img" aria-label="Portrait of Marcus Pellow"><div></div></div><h4>Marcus Pellow</h4><span>Founder and Principal</span><i></i></div>
  <div class="profile" style="left:365px"><div class="photo" role="img" aria-label="Portrait of Owen R. Castell"><div></div></div><h4>Owen R. Castell</h4><span>Attorney</span><i></i></div>
  <div class="profile" style="left:553px"><div class="photo" role="img" aria-label="Portrait of Julian S. Marlow"><div></div></div><h4>Julian S. Marlow</h4><span>Associate Attorney</span><i></i></div>
</section>

<section>
  <h2 class="abs h-section res-title">RESOURCES</h2>
  <div class="card" style="left:182px;top:2398px;width:244px;height:214px">
    <h4>Department of<br>Homeland Security (DHS)</h4>
    <dl><dt>U.S. Citizenship &amp; Immigration Se...</dt><dd>http://citizens.example/index.htm</dd>
    <dt>Bureau of Customs &amp; Border Pr...</dt><dd>http://www.border.example</dd></dl>
    <svg class="arrow" width="12" height="8" viewBox="0 0 12 8" fill="none" stroke="#0b3272" stroke-width="1.5"><path d="M0 4h11M8 1l3 3-3 3"/></svg>
  </div>
  <div class="card" style="left:444px;top:2398px;width:314px;height:512px">
    <h4>Department of Labor (DOL)</h4>
    <dl><dt>DOL Home Page</dt><dd>http://www.laborhub.example</dd>
    <dt>Dictionary of Occupational Titles</dt><dd>http://titles.laborhub.example/list.htm</dd>
    <dt>Employment &amp; Training Administration</dt><dd>http://www.trainingadmin.example</dd>
    <dt>Occupational Employment Statistics</dt><dd>http://www.laborstats.example/oes</dd>
    <dt>Occupational Outlook Handbook</dt><dd>http://www.laborstats.example/oco</dd>
    <dt>O*NET</dt><dd>http://www.jobcenter.example</dd>
    <dt>PERM</dt><dd>http://www.permdesk.example</dd></dl>
    <svg class="arrow" width="12" height="8" viewBox="0 0 12 8" fill="none" stroke="#0b3272" stroke-width="1.5"><path d="M0 4h11M8 1l3 3-3 3"/></svg>
  </div>
  <div class="card" style="left:774px;top:2398px;width:244px;height:214px">
    <h4>Department of<br>State (DOS)</h4>
    <dl><dt>DOS Home Page</dt><dd>http://www.state.example</dd>
    <dt>Bureau of Consular Affairs</dt><dd>http://travel.state.example</dd></dl>
    <svg class="arrow" width="12" height="8" viewBox="0 0 12 8" fill="none" stroke="#0b3272" stroke-width="1.5"><path d="M0 4h11M8 1l3 3-3 3"/></svg>
  </div>
  <div class="card" style="left:182px;top:2625px;width:244px;height:285px">
    <h4>Department of<br>Justice (DOJ)</h4>
    <dl><dt>Office of Special Counsel for Imm...</dt><dd>http://www.justice.example/osc</dd>
    <dt>Office for Special Counsel for...</dt><dd>http://www.justice.example/about/o...</dd>
    <dt>OSC Letter on Employment Veri...</dt><dd>http://www.justice.example/ab...</dd></dl>
    <svg class="arrow" width="12" height="8" viewBox="0 0 12 8" fill="none" stroke="#0b3272" stroke-width="1.5"><path d="M0 4h11M8 1l3 3-3 3"/></svg>
  </div>
  <div class="card" style="left:774px;top:2625px;width:244px;height:285px">
    <h4>Department of<br>State (DOS)</h4>
    <dl><dt>U.S. Consulates, Embassies, &amp; Mi...</dt><dd>http://embassy.state.example</dd>
    <dt>U.S. Visa Policy and Procedures</dt><dd>http://www.visas.example</dd>
    <dt>Visa Bulletin</dt><dd>http://travel.state.example/visa/b...</dd></dl>
    <svg class="arrow" width="12" height="8" viewBox="0 0 12 8" fill="none" stroke="#0b3272" stroke-width="1.5"><path d="M0 4h11M8 1l3 3-3 3"/></svg>
  </div>
  <span class="dot on" style="left:571px"></span>
  <span class="dot" style="left:595px"></span>
  <span class="dot" style="left:619px"></span>
</section>

<section>
  <div class="abs contact-bg" role="img" aria-label="Photograph of white columns and a domed government building"></div>
  <div class="abs contact-panel"></div>
  <h2 class="abs h-section contact-title">CONTACT US</h2>
  <div class="field" style="left:219px;top:3253px;width:165px;height:47px">Name</div>
  <div class="field" style="left:396px;top:3253px;width:166px;height:47px">Email</div>
  <div class="field" style="left:219px;top:3310px;width:343px;height:46px">Message</div>
  <a class="abs submit">SUBMIT</a>
  <div class="abs map" role="img" aria-label="Street map of the office area with a location pin">
    <svg class="abs" style="left:176px;top:128px" width="22" height="30" viewBox="0 0 22 30"><path d="M11 0C5 0 0 5 0 11c0 8 11 19 11 19s11-11 11-19C22 5 17 0 11 0z" fill="#d93025"/><circle cx="11" cy="11" r="4" fill="#8a1a14"/></svg>
  </div>
</section>

<footer>
  <div class="footer">
    <h5 style="left:115px;top:83px">ADDRESS</h5>
    <p style="left:115px;top:118px;width:340px">The Law Office of Marcus Pellow is located at 1200 Harbor Avenue Suite 410, Riverton CA 90000.</p>
    <svg class="icon" style="left:117px;top:178px" width="13" height="13" viewBox="0 0 13 13" fill="none" stroke="#ccc" stroke-width="1.2"><path d="M3 1l2 3-1 2c1 2 2 3 3 3l2-1 3 2-1 2C6 12 1 7 1 2z"/></svg>
    <p style="left:138px;top:173px">(555) 384-0142</p>
    <svg class="icon" style="left:117px;top:200px" width="13" height="10" viewBox="0 0 13 10" fill="none" stroke="#ccc" stroke-width="1.2"><rect x=".5" y=".5" width="12" height="9"/><path d="M.5 .5l6 5 6-5"/></svg>
    <p style="left:138px;top:194px">info@pellowlaw.example</p>
    <span class="social" style="left:116px"></span>
    <span class="social" style="left:144px"></span>
    <span class="social" style="left:172px"></span>
    <h5 style="left:505px;top:83px">CASE STATUS</h5>
    <div class="abs seal" role="img" aria-label="Agency badge"></div>
    <h5 style="left:747px;top:83px;width:330px">KNOWLEDGEABLE AND DEPENDABLE IMMIGRATION REPRESENTATION</h5>
    <p style="left:747px;top:142px;width:370px">U.S. immigration law is extremely complex, constantly changing and time consuming. Based on our vast experience in immigration law, our firm is able to provide comprehensive, well thought out solutions to your immigration needs.</p>
  </div>
  <div class="abs bottom">
    <span style="left:113px">© 2019 MARCUS PELLOW LAW OFFICES</span>
    <span style="left:829px">TERMS OF USE</span>
    <span style="left:931px">|</span>
    <span style="left:949px">RESOURCES</span>
    <span style="left:1041px">|</span>
    <span style="left:1059px">CONTACT</span>
  </div>
</footer>

</body>
</html>
```